Guaranteed Job - Sleek Sexy Business Card UV Spot

Im looking for a sleek and sexy business card, that resembles elite or VIP status status.
our business is corinvale.example
you can view our products on there, but our main audience for handing out our cards will be for people in the hospitality industry, so it will need to impress high management and CEO of hotels and restaurants, bars, clubs etc...
the card features will have UV spot on both sides, 400gsm stock. standard size.
Artwork should be 86 x 54mm + 2mm bleed = 90 x 58mm
it should have a nice "unique" uv spot pattern that highlights the card, not a repeated pattern, theres no originality there, and it will be disregarded.
The written material will be:
Corin Vale Hospitality College (logo)
Tobin Marsh
Director
Phone: 1300 615 737
Mobile: 0455 817 296
Email: info@corinvale.example
website: www.corinvale.example
I'm looking for originality here, i don't want just a simple stock card, want something that has a wow factor for people.
You will find the logo attached. you may invert the white to black words to suit the background as you please.
thank you and good luck
As a side note, ive received a lot of proposals, im too busy to give feedback to each and every one, so if i havent provided feedback for your design within 24 hours, then consider it not acceptable, and you could resubmit another design.
So far i have not seen any design that stood out for me, they all seem pretty generic. there nothing thats unique, i would figure for the amount that im offering, that people would put some more effort and creativity into the design.
so far over 200 designs submitted, and nothing i have seen looks very original, everything looks like a different variation of the same stuff, i said it very clearly i wanted something unique, the only thing that has come close to it so far is this one
Reason: Ive received alot of design concepts and i have reviewed everyone, but i havent had time to give feedback to every single one, only the ones that have interested me, if i havent responded, its because i havent found it good enough.
so far only a few design have been on par with what ive been looking for, an attractive eye popping design.
heres a few of them,
http://files.pixelbazaar.example/design_img/51736/62418/62418_2840915_51736_image.jpg
http://files.pixelbazaar.example/design_img/51736/68254/68254_2841377_51736_image.jpg
theyre, both unique and original, and eye catching, the only thing theyre missing is the sexyness.
if you still think you have some creativity left in your minds, then throw it on here.
Reason: Sorry guys for the delay, I was in a serious accident and out of commission for the past few months, I'm just slowly recovering now, please bare with me as i try to attend to this project, it may take me awhile as I have other projects that are on standby, I'm not 100% at the moment, so im extending the deadline for 2 weeks right now. Thanks for your patience.
Hospitality

```html
<!DOCTYPE html>
<html lang="en">
<head>
<meta charset="utf-8">
<title>Corin Vale Hospitality College – Business Card</title>
<link rel="stylesheet" href="https://fonts.googleapis.com/css2?family=Ubuntu:wght@500;700&family=Roboto+Condensed:wght@800&family=Arimo:wght@700&display=swap">
<style>
  :root {
    --teal: #4bbeb1;
    --lime: #c8e68a;
    --ink: #1b1b1b;
    --white: #ffffff;
    --blue: #1e9ad6;
  }
  * { margin: 0; padding: 0; box-sizing: border-box; }
  html, body { width: 1200px; height: 769px; overflow: hidden; background: var(--teal); }
  .card {
    position: relative;
    width: 1200px;
    height: 769px;
    background: var(--teal);
    overflow: hidden;
  }
  .brand-panel {
    position: absolute;
    left: 0; top: 0;
    width: 838px; height: 420px;
    background: var(--lime);
  }
  .website {
    position: absolute;
    right: 30px; top: 56px;
    font-family: "Arimo", Arial, sans-serif;
    font-weight: 700;
    font-size: 41px;
    color: var(--white);
    letter-spacing: 0.2px;
  }
  .brand {
    position: absolute;
    left: 56px; top: 150px;
    display: flex;
    align-items: center;
    gap: 44px;
  }
  .brand-mark {
    width: 180px; height: 180px;
    background: var(--blue);
    flex: none;
  }
  .brand-name {
    font-family: "Ubuntu", Arial, sans-serif;
    font-weight: 500;
    font-size: 54px;
    line-height: 1.05;
    color: var(--ink);
  }
  .person {
    position: absolute;
    right: 366px; top: 436px;
    text-align: right;
    font-family: "Ubuntu", Arial, sans-serif;
    font-weight: 700;
    color: var(--ink);
  }
  .person-name { font-size: 57px; line-height: 1.1; }
  .person-title { font-size: 37px; line-height: 1.3; }
  .contacts {
    position: absolute;
    left: 36px; right: 30px; top: 676px;
    height: 74px;
    display: flex;
    align-items: center;
    font-family: "Roboto Condensed", "Arial Narrow", sans-serif;
    font-weight: 800;
    font-size: 26px;
    color: var(--ink);
    white-space: nowrap;
  }
  .contact-item { padding: 0 8px; }
  .contact-item:first-child { padding-left: 0; }
  .divider {
    width: 3px; height: 74px;
    background: var(--ink);
    flex: none;
  }
</style>
</head>
<body>
  <main class="card">
    <div class="brand-panel"></div>
    <p class="website">www.corinvale.example</p>

    <div class="brand">
      <span class="brand-mark" aria-hidden="true"></span>
      <p class="brand-name">Corin Vale<br>Hospitality<br>College</p>
    </div>

    <div class="person">
      <p class="person-name">Tobin Marsh</p>
      <p class="person-title">Direktur</p>
    </div>

    <div class="contacts">
      <span class="contact-item">Telepon : 1300 615 737</span>
      <span class="divider"></span>
      <span class="contact-item">Handphone : 0455 817 296</span>
      <span class="divider"></span>
      <span class="contact-item">email : info@corinvale.example</span>
    </div>
  </main>
</body>
</html>
```